Posters for diabetes webinar and detox webinar promotion

I am creating a webinar for people to sign in for lead generation

1. Pre heading: Free training for people dealing with Pre-Diabetes or Type 2 Diabetes.
Heading: The HARBORLIGHT Coaching Method. A Unique Path To An Insulin-Free Life.
subheading: Delphine went from 80 units to 0 in less than 30 days, and you could too.
Sign up now!

2. detox webinar : Pre-Headline: Exclusive Free Training for Anyone Struggling with Chronic Health Conditions
Headline: The HARBORLIGHT Detox Masterclass
A Revolutionary Way to Reset Your Health
Subheading: Subheading: "Learn How Ruth Overcame 10 Autoimmune Conditions, Eliminated Pain, and Rediscovered the Joy of Eating in Just 10 Days. You Can Too.

Sign up now!

Logo (use only Harborlight. no need to have the health care)
https://files.quorvanshare.com/folders/7Hq2LmPx9WeTz4NcVb3RkYs8JdGfUa?usp=share_link

posters color samples that I like

https://files.quorvanshare.com/folders/82pmWqTzRb5LkHvNcY7XeJsQaDgFuP?usp=share_link

website https://sugarbalancepath.health
our target audience for our upcoming campaigns. We're zooming in on the wonderful folks here in Hawaii, mostly within the Asian community.

For our diabetes reversal campaign, think 45+ in age. For the detox initiative, aim for the 30+ crowd. This should help us tailor our designs to really resonate with them.

One more thing! Could you please leave some white space on the posters for dates? I won't be printing them directly but would like the option to slap on a white sticker that blends well with the overall design.

I want to able to make it in different size but actually 24in x 36in, 36in x 48in. I am looking for a clean look. I really like the colors in the drive specially the style and design where it says about "Today is the day for healthier you" not this text I wanted in the poster but the style I like. and actually the little icons surrounding this sentence can be then icons of my Harborlight method if you can do that.

R - Right Nutrition
E - Exercise
S - Sunlight
T - Temperance
O - Optimal water intake
R - Rest
A - Air
T - Trust in divine power
I - Initiating social support
O - Optimism
N - Nature

Please look at the sample design and the colours that I send

the audience that I am trying to target is the people of Hawaii mostly. most of the people are asians.
for diabetes poster the age is 50+
for detox poster the age is 30+

Target Market(s)

50+ for diabetes and 30+

Industry/Entity Type

Health and wellness

Colors
0054AA
0677BA
7BADD7
CADEEF
E8F1F8
6B429C
8869AF
B7A5CE
E3DAEB
F3F0F8

Requirements
Nice to have
• the concept of this not the content. https://files.quorvanshare.com/file/d/4KtwPzRnMb8QxLcVh2JsYeGdFaNu5T/view?usp=sharing
Should not have
• too crowded

```html
<!DOCTYPE html>
<html lang="en">
<head>
<meta charset="utf-8">
<title>Harborlight Webinar Posters</title>
<link href="https://fonts.googleapis.com/css2?family=Bebas+Neue&family=Playball&family=Poppins:wght@400;500;600;700;800&family=Michroma&display=swap" rel="stylesheet">
<style>
  :root{
    --navy:#262f5c;
    --navy-deep:#1f274f;
    --green:#6bbd3c;
    --green-light:#9fd27e;
    --green-pale:#cfe8bd;
    --white:#ffffff;
    --stage:#dedede;
  }
  *{margin:0;padding:0;box-sizing:border-box}
  html,body{width:800px;height:1200px;overflow:hidden;background:var(--stage)}
  .stage{position:relative;width:800px;height:1200px}
  .poster{position:absolute;left:143px;width:514px;height:514px;background:var(--white);overflow:hidden}
  .poster--diabetes{top:74px}
  .poster--detox{top:622px}
  .abs{position:absolute}
  .label-wide{font-family:"Michroma",sans-serif;font-weight:400;font-size:12px;letter-spacing:.5px;color:var(--white);white-space:nowrap}
  .label-wide .accent{color:var(--green)}
  .small-copy{font-family:"Poppins",sans-serif;font-size:9px;line-height:10px;color:var(--white)}
  .headline{font-family:"Bebas Neue",sans-serif;color:var(--green);font-size:38px;line-height:34px;white-space:nowrap}
  .script{font-family:"Playball",cursive;color:var(--white);font-size:28px;line-height:30px;white-space:nowrap}
  .rule{height:1px;background:var(--green)}
  .rule::after{content:"";position:absolute;right:0;top:-1px;width:30px;height:2px;background:var(--green)}
  .photo{background:linear-gradient(135deg,#e9f3f8,#bcd8ea 60%,#4a86d4)}
  .date-badge{border-radius:50%;background:var(--navy);border:6px solid var(--green)}
  .date-text{font-family:"Bebas Neue",sans-serif;white-space:nowrap;line-height:1}
  .date-day{color:var(--green);font-size:34px}
  .date-time{color:var(--white);font-family:"Poppins",sans-serif;font-weight:600;font-size:12px}
  .date-time::before{content:"";display:inline-block;width:20px;height:2px;background:var(--white);vertical-align:middle;margin-right:14px}
  .date-weekday{color:var(--white);font-size:36px}
  .pill{border-radius:20px;background:var(--navy);font-family:"Poppins",sans-serif;font-weight:700;color:var(--white);display:flex;align-items:center;justify-content:center;white-space:nowrap}
  .brand{display:flex;align-items:center;gap:10px}
  .brand-mark{border-radius:50%;background:var(--green)}
  .brand-name{font-family:"Poppins",sans-serif;font-weight:700;letter-spacing:-.5px}
</style>
</head>
<body>
<main class="stage">

  <!-- Diabetes webinar poster -->
  <section class="poster poster--diabetes">
    <div class="abs" style="left:0;top:0;width:291px;height:422px;background:var(--navy)"></div>
    <div class="abs" style="left:291px;top:0;width:4px;height:422px;background:var(--green)"></div>
    <div class="abs photo" style="left:295px;top:0;width:219px;height:422px" role="img" aria-label="Photo of a blue blood glucose meter with test strip and stethoscope"></div>

    <div class="abs label-wide" style="left:24px;top:27px"><span class="accent">FREE</span> TRAINING</div>
    <div class="abs small-copy" style="left:24px;top:43px">For people dealing with<br>Pre-Diabetes or</div>
    <div class="abs" style="left:144px;top:41px;font-family:'Bebas Neue',sans-serif;color:var(--white);font-size:22px">OR</div>
    <div class="abs" style="left:170px;top:37px;font-family:'Poppins',sans-serif;font-weight:800;color:var(--green);font-size:26px;line-height:26px">2</div>
    <div class="abs" style="left:197px;top:44px;background:var(--green);color:var(--white);font-family:'Poppins',sans-serif;font-weight:700;font-size:7px;padding:0 3px;line-height:9px">TYPE</div>
    <div class="abs" style="left:196px;top:55px;color:var(--white);font-family:'Poppins',sans-serif;font-weight:700;font-size:7.5px">DIABETES</div>

    <h1 class="abs headline" style="left:24px;top:84px">THE HARBORLIGHT</h1>
    <div class="abs script" style="left:24px;top:108px">Coaching Method</div>
    <h2 class="abs headline" style="left:24px;top:150px">A UNIQUE PATH TO AN</h2>
    <div class="abs script" style="left:24px;top:175px">Insulin Free Life</div>
    <div class="abs rule" style="left:24px;top:220px;width:249px"></div>

    <p class="abs" style="left:24px;top:236px;font-family:'Poppins',sans-serif;color:var(--white);font-size:12px;line-height:15px;font-weight:700">
      <span style="font-weight:500">Delphine went from</span><br>
      <span style="color:var(--green)">80 UNITS</span> TO <span style="color:var(--green)">0 IN LESS</span><br>
      THAN 30 DAYS, &amp; YOU COULD TOO.
    </p>
    <div class="abs" style="left:24px;top:293px;width:130px;height:14px;background:var(--green);color:var(--white);font-family:'Poppins',sans-serif;font-weight:700;font-size:8.5px;line-height:14px;padding-left:5px">BOOK YOUR <span style="color:#d9f0c7">SEAT NOW</span></div>
    <div class="abs" style="left:24px;top:311px;font-family:'Poppins',sans-serif;font-weight:600;color:var(--white);font-size:12.5px">www.<span style="color:var(--green)">sugarbalancepath</span>.health</div>

    <div class="abs" style="left:0;top:337px;width:200px;height:90px;background:linear-gradient(90deg,#2c3a80,#1f45c4 60%,#8a93a8)" role="img" aria-label="Photo of a blue 'Diabetes Type 2' binder with stethoscope and magnifier"></div>

    <div class="abs brand" style="left:24px;top:448px">
      <div class="brand-mark" style="width:34px;height:34px"></div>
      <div class="brand-name" style="color:var(--navy);font-size:21px">HARBORLIGHT</div>
    </div>

    <div class="abs date-badge" style="left:311px;top:329px;width:164px;height:164px"></div>
    <div class="abs date-text date-day" style="left:350px;top:359px">08 SEP</div>
    <div class="abs date-text date-time" style="left:350px;top:393px">4 PM</div>
    <div class="abs date-text date-weekday" style="left:350px;top:403px">FRIDAY</div>

    <div class="abs pill" style="left:284px;top:450px;width:211px;height:38px;font-size:21px">SIGN UP&nbsp;<span style="color:var(--green)">NOW!</span></div>

    <svg class="abs" style="left:0;top:502px" width="514" height="12" viewBox="0 0 514 12" aria-hidden="true">
      <polygon points="0,0 44,0 56,12 0,12" fill="var(--green)"/>
      <polygon points="69,0 128,0 140,12 81,12" fill="var(--green)" opacity=".7"/>
      <polygon points="153,0 212,0 224,12 165,12" fill="var(--green)" opacity=".4"/>
      <polygon points="237,0 296,0 308,12 249,12" fill="var(--green)" opacity=".2"/>
    </svg>
  </section>

  <!-- Detox masterclass poster -->
  <section class="poster poster--detox">
    <div class="abs" style="left:0;top:0;width:514px;height:278px;background:var(--navy)"></div>

    <div class="abs label-wide" style="left:24px;top:26px"><span class="accent">EXCLUSIVE FREE</span> TRAINING FOR</div>
    <div class="abs small-copy" style="left:26px;top:44px">Anyone Struggling with</div>
    <div class="abs" style="left:140px;top:43px;background:var(--green);color:var(--white);font-family:'Poppins',sans-serif;font-weight:700;font-size:7.5px;line-height:10px;padding:0 5px">CHRONIC HEALTH CONDITIONS</div>

    <div class="abs brand-mark" style="left:385px;top:30px;width:50px;height:50px"></div>
    <div class="abs brand-name" style="left:328px;top:88px;width:162px;text-align:center;color:var(--white);font-size:21px">HARBORLIGHT</div>

    <h1 class="abs headline" style="left:24px;top:83px">THE HARBORLIGHT</h1>
    <div class="abs script" style="left:24px;top:107px">Detox Masterclass</div>
    <h2 class="abs headline" style="left:31px;top:152px">A REVOLUTIONARY WAY TO</h2>
    <div class="abs script" style="left:24px;top:177px">Reset Your Health</div>
    <div class="abs rule" style="left:24px;top:224px;width:313px"></div>

    <div class="abs" style="left:24px;top:258px;width:387px;height:106px;background:var(--green)"></div>
    <p class="abs" style="left:51px;top:271px;font-family:'Poppins',sans-serif;color:var(--white);font-size:12.5px;font-weight:500">Learn How Ruth Overcame</p>
    <p class="abs" style="left:51px;top:294px;font-family:'Poppins',sans-serif;color:var(--navy-deep);font-size:8.3px;line-height:13px;font-weight:500">10 AUTOIMMUNE CONDITIONS, ELIMINATED PAIN, AND<br>REDISCOVERED THE JOY OF EATING IN JUST 10 DAYS.</p>
    <p class="abs" style="left:51px;top:326px;font-family:'Poppins',sans-serif;color:var(--navy-deep);font-size:12px;font-weight:500">You Can Too.</p>

    <div class="abs" style="left:370px;top:145px;width:144px;height:230px;background:linear-gradient(160deg,#c9d4e0,#f1ede6 55%,#4e6fb8)" role="img" aria-label="Photo of a smiling older couple on a picnic blanket"></div>
    <div class="abs" style="left:265px;top:295px;width:105px;height:78px;background:linear-gradient(135deg,#e9a25a,#8a5a2e 60%,#3e62b0)" role="img" aria-label="Photo of a picnic basket with tulips on a checked blanket"></div>

    <svg class="abs" style="left:240px;top:390px" width="274" height="13" viewBox="0 0 274 13" aria-hidden="true">
      <polygon points="0,0 50,0 62,13 12,13" fill="var(--green)" opacity=".2"/>
      <polygon points="74,0 124,0 136,13 86,13" fill="var(--green)" opacity=".4"/>
      <polygon points="148,0 198,0 210,13 160,13" fill="var(--green)" opacity=".7"/>
      <polygon points="222,0 274,0 274,13 234,13" fill="var(--green)"/>
    </svg>

    <div class="abs" style="left:0;top:370px;width:300px;height:118px;overflow:hidden">
      <div class="abs date-badge" style="left:117px;top:2px;width:148px;height:148px"></div>
    </div>
    <div class="abs" style="left:18px;top:372px;width:110px;height:126px;background:linear-gradient(180deg,#f0a330,#c9d3e3 60%,#9aa3ad)" role="img" aria-label="Illustration of an anatomical body model with stethoscope and 'Health' tag"></div>
    <div class="abs date-text date-day" style="left:148px;top:400px">09 SEP</div>
    <div class="abs date-text date-time" style="left:148px;top:434px">4 PM</div>
    <div class="abs date-text date-weekday" style="left:148px;top:444px">FRIDAY</div>

    <div class="abs pill" style="left:312px;top:416px;width:134px;height:38px;font-size:21px">SIGN UP</div>
    <div class="abs" style="left:312px;top:456px;width:134px;text-align:center;font-family:'Poppins',sans-serif;font-weight:800;color:var(--green);font-size:22px">NOW!</div>
    <div class="abs rule" style="left:250px;top:488px;width:240px"></div>

    <svg class="abs" style="left:0;top:502px" width="514" height="12" viewBox="0 0 514 12" aria-hidden="true">
      <polygon points="0,0 271,0 259,12 0,12" fill="var(--green)"/>
      <polygon points="295,0 354,0 342,12 283,12" fill="var(--green)" opacity=".7"/>
      <polygon points="379,0 438,0 426,12 367,12" fill="var(--green)" opacity=".4"/>
      <polygon points="463,0 514,0 514,12 451,12" fill="var(--green)" opacity=".2"/>
    </svg>
  </section>

</main>
</body>
</html>
```